Company Broshure Oil&Energy Industry

We have recently completed a company rebranding, and our new website is now fully live and available at www.velmorquist.ro.

To ensure consistency across all communication materials, we would like to redesign our company presentation flyer/brochure so that it fully reflects the updated branding and visual identity of the website.

Please find attached our current brochure (last item uploaded on the list), which should be redesigned in line with the new website’s look and feel. The overall structure and text content should remain unchanged; only the layout and visual design need to be updated. I have uploaded pictures from of the website theme. Can be used by designers for the new design.
Updates

We uploaded pictures belonging to website design theme that can be used for the new brochure.

Target Market(s)

EPC Contractors

Industry/Entity Type

Oil&Energy

Font styles to use
Other font styles liked:
• Calibri

Colors
0094D4
00A9DD
6FCCEA
C7EBF8
E9F6FB

Requirements
Must have
• a clear structure, elegant layout
Nice to have
• I would like to have a dynamic approach. To feel elegant and alive.

```html
<!DOCTYPE html>
<html lang="en">
<head>
<meta charset="utf-8">
<title>Velmorquist Group – Company Brochure</title>
<link href="https://fonts.googleapis.com/css2?family=Poppins:ital,wght@0,400;0,500;0,600;0,700;0,800;1,500;1,600;1,700&display=swap" rel="stylesheet">
<style>
  :root{
    --blue:#1a95d5;
    --blue-bright:#0fa3de;
    --orange:#f47521;
    --ink:#1d1d1f;
    --stage:#dcdcdc;
    --paper:#ffffff;
  }
  *{margin:0;padding:0;box-sizing:border-box}
  html,body{width:833px;height:1200px;overflow:hidden}
  body{background:var(--stage);font-family:'Poppins',sans-serif;color:var(--ink);position:relative}

  .spread{position:absolute;left:105px;width:623px;height:481px;display:flex}
  .spread--cover{top:95px}
  .spread--inside{top:624px}
  .page{position:relative;width:311.5px;height:100%;overflow:hidden;background:var(--paper)}

  /* back cover */
  .back-cover{background:linear-gradient(160deg,#2a9ddb 0%,#1b8fcf 55%,#2283c4 100%);color:#fff}
  .back-cover__photo{position:absolute;inset:0;background:
      linear-gradient(180deg,rgba(255,255,255,0) 0%,rgba(20,70,120,.18) 45%,rgba(10,50,95,.22) 100%)}
  .brandmark{position:absolute;top:118px;left:26px;color:#fff}
  .brandmark__name{font-weight:500;font-size:38px;line-height:1;letter-spacing:3px}
  .brandmark__sub{font-size:6.3px;font-weight:500;letter-spacing:.2px;margin-top:3px}
  .back-cover__headline{position:absolute;left:26px;top:216px;font-weight:800;font-size:38px;line-height:39.2px;letter-spacing:.3px}
  .contacts{position:absolute;left:26px;top:494px;list-style:none;font-style:italic;font-weight:500;font-size:8px}
  .contacts li{display:flex;align-items:center;height:12.8px}
  .contacts svg{width:8px;height:8px;margin-right:6px;flex:none}
  .contacts .indent{padding-left:14px}

  /* front cover */
  .front-cover__brandmark{position:absolute;top:118px;left:0;right:0;text-align:center;color:var(--orange)}
  .front-cover__brandmark .brandmark__sub{color:var(--ink)}
  .front-cover__title{position:absolute;top:206px;left:0;right:0;text-align:center;font-weight:800;line-height:1}
  .front-cover__title .l1{display:block;font-size:52px;color:var(--blue);line-height:46px}
  .front-cover__title .l2{display:block;font-size:34px;color:var(--orange);line-height:32px;letter-spacing:1px}
  .front-cover__title .l3{display:block;font-size:58px;color:var(--blue-bright);line-height:50px}
  .front-cover__photo{position:absolute;left:0;right:0;top:340px;bottom:0;
      background:linear-gradient(180deg,#ffffff 0%,#eef0f6 12%,#c9d0e2 32%,#8f97b0 58%,#5a5d6e 80%,#3b3c47 100%)}
  .front-cover__tagline{position:absolute;top:348px;left:0;right:0;text-align:center;font-style:italic;font-weight:600;font-size:12.5px;line-height:14px}
  .front-cover__url{position:absolute;bottom:12px;left:0;right:0;text-align:center;color:#fff;font-style:italic;font-weight:600;font-size:9.5px}

  /* inside pages */
  .content{position:absolute;left:26px;width:259px}
  .page--right .content{left:25.5px}
  .heading{font-weight:800;line-height:.98;letter-spacing:.2px}
  .heading--orange{color:var(--orange)}
  .heading--blue{color:var(--blue)}
  .heading--xl{font-size:24.5px}
  .heading--l{font-size:23px}
  .copy{font-size:6.15px;line-height:8.65px;text-align:justify;font-weight:500}

  .services{list-style:none;margin-top:5px}
  .services li{display:flex;font-size:6.6px;line-height:8.6px;font-weight:500;margin-bottom:3.1px}
  .services svg{width:6.5px;height:6.5px;flex:none;margin:1px 3.5px 0 0}

  .sectors{display:grid;grid-template-columns:128px 127px;column-gap:4px;row-gap:5px;margin-top:5px}
  .sector{height:19.5px;display:flex;align-items:center;justify-content:center;color:#fff;font-weight:600;font-size:9.8px;letter-spacing:.3px}
  .sector--blue{background:var(--blue)}
  .sector--orange{background:var(--orange)}

  .page--right{background:linear-gradient(90deg,#dadada 0%,#f1f1f1 6%,#ffffff 14%)}
  .partners{display:flex;align-items:center;justify-content:space-between;height:32px}
  .partners--second{justify-content:center;gap:16px;margin-top:12px}
  .partner{display:flex;align-items:center;gap:3px;font-weight:600;font-size:9px;color:#3a3a3a}
  .partner--lg{font-size:14px}
  .partner__dot{width:7px;height:7px;background:var(--orange);flex:none}
  .inside-photo{position:absolute;left:0;right:0;bottom:0;height:150px;
      background:linear-gradient(180deg,rgba(255,255,255,1) 0%,rgba(230,233,240,.9) 18%,#b9c0d0 45%,#7d8296 72%,#4a4b58 100%)}
</style>
</head>
<body>

<section class="spread spread--cover">
  <article class="page back-cover">
    <div class="back-cover__photo" role="img" aria-label="Blue-toned photo of an industrial plant structure"></div>
    <div class="brandmark">
      <div class="brandmark__name">VQG</div>
      <div class="brandmark__sub">VELMORQUIST GROUP</div>
    </div>
    <h2 class="back-cover__headline">YOUR<br>VALUABLE<br>PARTNER<br>FOR OIL &amp;<br>ENERGY<br>PROJECTS</h2>
    <ul class="contacts">
      <li><svg viewBox="0 0 10 10"><circle cx="5" cy="5" r="5" fill="#fff"/><path d="M2.6 3.5h4.8v3.2H2.6z M2.6 3.5L5 5.3 7.4 3.5" fill="none" stroke="#1a95d5" stroke-width=".8"/></svg>office@velmorquist.ro</li>
      <li><svg viewBox="0 0 10 10"><circle cx="5" cy="5" r="5" fill="#fff"/><circle cx="5" cy="5" r="2.7" fill="none" stroke="#1a95d5" stroke-width=".7"/><path d="M2.3 5h5.4M5 2.3c-1.4 1.6-1.4 3.8 0 5.4M5 2.3c1.4 1.6 1.4 3.8 0 5.4" fill="none" stroke="#1a95d5" stroke-width=".6"/></svg>www.velmorquist.ro</li>
      <li><svg viewBox="0 0 10 10"><path d="M5 0.3C2.9.3 1.4 1.9 1.4 3.8 1.4 6.4 5 9.7 5 9.7s3.6-3.3 3.6-5.9C8.6 1.9 7.1.3 5 .3z" fill="#fff"/><circle cx="5" cy="3.8" r="1.3" fill="#1a95d5"/></svg>Str. Lindenau, no.7</li>
      <li class="indent">Bucharest, Romania</li>
      <li><svg viewBox="0 0 10 10"><circle cx="5" cy="5" r="5" fill="#fff"/><rect x="3.4" y="2.2" width="3.2" height="5.6" rx=".6" fill="#1a95d5"/></svg>0040700555010</li>
    </ul>
  </article>

  <article class="page front-cover">
    <div class="front-cover__photo" role="img" aria-label="Night photo of a refinery with illuminated storage tanks"></div>
    <div class="brandmark front-cover__brandmark" style="left:0;right:0">
      <div class="brandmark__name">VQG</div>
      <div class="brandmark__sub">VELMORQUIST GROUP</div>
    </div>
    <h1 class="front-cover__title">
      <span class="l1">VELMOR</span>
      <span class="l2">QUIST</span>
      <span class="l3">GROUP</span>
    </h1>
    <p class="front-cover__tagline">YOUR VALUABLE PARTNER<br>FOR OIL &amp;ENERGY PROJECTS</p>
    <p class="front-cover__url">www.velmorquist.ro</p>
  </article>
</section>

<section class="spread spread--inside">
  <article class="page page--left">
    <div class="content" style="top:26px">
      <h2 class="heading heading--orange heading--xl">WHO<br>WE ARE</h2>
      <p class="copy" style="margin-top:3px">Velmorquist Group is a Romanian registred company, founded in 2003. We have been active in Oil&amp;Energy industry serving local and international market by sourcing highly specilised professionals for Oil&amp;Energy projects. We offer a wide range of services that encompass every stage of the process, starting from the initial selection of professionals and extending to the management of employment and logistics (mobilisation) for the assigned resources. Whether the project is located domestically or abroad, we offer tailored support to ensure successful project completion for our clients.</p>

      <h2 class="heading heading--blue heading--l" style="margin-top:10px">SERVICES</h2>
      <ul class="services">
        <li><svg viewBox="0 0 10 10"><circle cx="5" cy="5" r="4.3" fill="none" stroke="#f47521" stroke-width="1.2"/><path d="M3 5.1l1.5 1.5L7.4 3.6" fill="none" stroke="#f47521" stroke-width="1.3"/></svg>Discipline Site Supervision (mechanical, electric, I&amp;C, piping)</li>
        <li><svg viewBox="0 0 10 10"><circle cx="5" cy="5" r="4.3" fill="none" stroke="#f47521" stroke-width="1.2"/><path d="M3 5.1l1.5 1.5L7.4 3.6" fill="none" stroke="#f47521" stroke-width="1.3"/></svg>Site Management (Construction/Commissioning)</li>
        <li><svg viewBox="0 0 10 10"><circle cx="5" cy="5" r="4.3" fill="none" stroke="#f47521" stroke-width="1.2"/><path d="M3 5.1l1.5 1.5L7.4 3.6" fill="none" stroke="#f47521" stroke-width="1.3"/></svg>Project Service Management (Planning, Cost Control/Estimate, Project Control, Document Controlling, Contract Control, Procurement)</li>
        <li><svg viewBox="0 0 10 10"><circle cx="5" cy="5" r="4.3" fill="none" stroke="#f47521" stroke-width="1.2"/><path d="M3 5.1l1.5 1.5L7.4 3.6" fill="none" stroke="#f47521" stroke-width="1.3"/></svg>Quality Control, Quality Assurance</li>
        <li><svg viewBox="0 0 10 10"><circle cx="5" cy="5" r="4.3" fill="none" stroke="#f47521" stroke-width="1.2"/><path d="M3 5.1l1.5 1.5L7.4 3.6" fill="none" stroke="#f47521" stroke-width="1.3"/></svg>HSE supervision, HSE Management</li>
        <li><svg viewBox="0 0 10 10"><circle cx="5" cy="5" r="4.3" fill="none" stroke="#f47521" stroke-width="1.2"/><path d="M3 5.1l1.5 1.5L7.4 3.6" fill="none" stroke="#f47521" stroke-width="1.3"/></svg>Welding &amp; NDT inspections</li>
        <li><svg viewBox="0 0 10 10"><circle cx="5" cy="5" r="4.3" fill="none" stroke="#f47521" stroke-width="1.2"/><path d="M3 5.1l1.5 1.5L7.4 3.6" fill="none" stroke="#f47521" stroke-width="1.3"/></svg>Discipline Engineering (process, piping, stress piping, instrument, electric, civil)</li>
      </ul>

      <h2 class="heading heading--orange heading--xl" style="margin-top:7px">INDUSTRY<br>WE SERVE</h2>
      <p class="copy" style="margin-top:3px">We are active in Oil&amp; Energy sector with hands on experience in upstream and downstream projects either brown or green field. Over the years we got involved in various projects within Refineries, LNG-s, Pipelines, Offshore Platforms, Power Plants (simple or combined cycle), Nuclear Power Plants and not least renewable from solar to wind or biomass. Having a large network of Romanian specialists available for mobilisation for projects inland and across the globe, we can respond quickly to clients’ requests by proposing the best available resources on the market.</p>

      <div class="sectors">
        <div class="sector sector--blue">OIL AND GAS</div>
        <div class="sector sector--orange">POWER</div>
        <div class="sector sector--orange">PETROCHEMISTRY</div>
        <div class="sector sector--blue">PHARMA</div>
      </div>
    </div>
  </article>

  <article class="page page--right">
    <div class="inside-photo" role="img" aria-label="Faded photo of refinery storage tanks at dusk"></div>
    <div class="content" style="top:25px">
      <h2 class="heading heading--orange heading--l">REFFERECES</h2>
      <p class="copy" style="margin-top:9px">We are collaborating with esteemed EPC contractors, Owners, and Engineering companies, offering comprehensive teams for durations ranging from 3 to 6 months or longer. Our support is essential during crucial phases such as turnarounds, construction, or commissioning. VQG provides the necessary expertise and manpower to expedite ongoing projects, ensuring timely completion for our clients.</p>

      <div class="partners" style="margin-top:10px">
        <span class="partner"><span class="partner__dot"></span>Harwell</span>
        <span class="partner">Dalmar</span>
        <span class="partner">Delfaro</span>
        <span class="partner">Mirathos</span>
      </div>
      <div class="partners partners--second">
        <span class="partner partner--lg">Ansenor Energia</span>
        <span class="partner partner--lg">Tidewell</span>
        <span class="partner partner--lg">Quorra</span>
      </div>

      <h2 class="heading heading--orange heading--l" style="margin-top:10px">WHEN VQG?</h2>
      <p class="copy" style="margin-top:6px">Whether you require a seasoned expert or a specialized team for your project, or if you're seeking to enhance your existing team with the right talent, we are here to assist. Velmorquist Group is dedicated to your project team efficiently and cost-effectively!</p>

      <h2 class="heading heading--orange heading--l" style="margin-top:10px">OUR PHILOSOPHY</h2>
      <p class="copy" style="margin-top:6px">Daily, we realize the world is remarkably interconnected. With decades of experience, we've come to appreciate the enduring value of human relationships—much like fine wine, they grow richer with time. Through our journey, we've cultivated a robust network of trusted professionals who rely on us just as much as we rely on them. Despite the inevitable mistakes we've made, each one served a purpose, guiding us towards improvement. Ultimately, it's our reputation that speaks volumes about the quality of our service.</p>
    </div>
  </article>
</section>

</body>
</html>
```